Zielgruppe
Ich habe derzeit 3 Geschäftsfelder:
-> HR Business Partner
-> Mediation
-> Coaching
Ich arbeite zum Einen prozesshaft und klar strukturiert, zum Anderen mit Kreativität und Empathie
Ich möchte Unternehmen bei diversen HR Aufgaben unterstützen wie z.B. Mitarbeitergespräche, Konfliktgespräche, Recruiting, Teambuilding, Prozessbegleitung und Workshops,...
als auch Unternehmen und Privatpersonen in Konfliktsituationen durch Mediationsprozesse führen (von Lehrlingsmediationen über Unternehmensübergaben und Wirtschaftsmediationen bis Paarmediationen, Nachbarschaftsmediationen, Familienmediationen,...)
Beim Coaching geht es um Karriere- und Bewerbungscoaching und auch Krisen- oder Beziehungscoaching (für Paare/ Familien)
In Zukunft möchte ich noch eine Ausbildung zur Outdoortrainerin machen um Teambuilding in der Natur anbieten zu können.
Aufgabenstellung
schlicht, unkompliziert, klare Struktur
nicht zu schnörkelig, verspielt
Naturbezug? ... eventuell als Schriftfarbe Rasen oder etwas in der Art als eyecatcher?
gut vorstellbar wären Farben in Kombination blau oder blaugrau mit grün?

```html
<!DOCTYPE html>
<html lang="de">
<head>
<meta charset="utf-8">
<title>Klarweg – Geschäftsausstattung</title>
<link href="https://fonts.googleapis.com/css2?family=Open+Sans:wght@400;600;700&display=swap" rel="stylesheet">
<style>
:root{
  --blue:#1f5ca8;
  --green:#30ab85;
  --ink:#2b2b2b;
  --muted:#7a7a7a;
  --paper:#f7f7f5;
  --sheet:#fbfbfb;
  --bg:#ececec;
  --window:#e4e4e4;
}
*{margin:0;padding:0;box-sizing:border-box}
html,body{width:698px;height:1200px;overflow:hidden;background:var(--bg);font-family:"Open Sans",Arial,sans-serif;color:var(--ink)}
.canvas{position:relative;width:698px;height:1200px}
.card{position:absolute;width:159px;height:91px;background:var(--paper);box-shadow:0 1px 3px rgba(0,0,0,.18);overflow:hidden}
.brand{position:absolute;display:flex;flex-direction:column;align-items:center;gap:4px}
.brand-dot{width:22px;height:22px;border-radius:50%;background:var(--blue)}
.brand-name{font-size:8.6px;font-weight:600;letter-spacing:1.1px;color:var(--blue);line-height:1;white-space:nowrap}
.card-front .brand{left:9px;top:8px;width:66px}
.card-decor{position:absolute;left:78px;top:14px;width:81px;height:77px;border-top-left-radius:46px;background:linear-gradient(180deg,var(--blue) 0%,var(--blue) 55%,var(--green) 100%)}
.card-back .brand{left:76px;top:11px;width:70px}
.card-tagline{position:absolute;left:10px;top:24px;font-size:4.8px}
.card-address,.card-contact{position:absolute;top:61px;font-size:3.4px;line-height:4.1px}
.card-address{left:11px}
.card-contact{left:99px}
.card-band{position:absolute;left:0;bottom:0;width:159px;height:9px}
.letter{position:absolute;width:247px;height:352px;background:var(--sheet);box-shadow:0 1px 4px rgba(0,0,0,.18)}
.letter .brand{top:10px}
.letter-left .brand{left:20px;width:58px}
.letter-right .brand{right:14px;width:58px}
.letter .brand-dot{width:21px;height:21px}
.letter .brand-name{font-size:8px}
.sender-line{position:absolute;left:19px;top:53px;font-size:2.8px;border-bottom:.5px solid var(--ink);padding-bottom:1px}
.recipient{position:absolute;left:27px;top:74px;font-size:3.6px;line-height:5.3px;color:var(--muted)}
.recipient-name{font-size:5.4px;font-weight:600;color:var(--ink);margin-bottom:2px;line-height:6px}
.letter-date{position:absolute;right:28px;top:100px;font-size:3.6px;color:var(--muted)}
.letter-body{position:absolute;left:27px;top:118px;width:192px;font-size:3.55px;line-height:5.4px;color:var(--muted);text-align:justify}
.letter-body p{margin-bottom:5.4px}
.signature{position:absolute;left:27px;top:254px;width:46px;height:10px;background:linear-gradient(90deg,#555,#999);opacity:.55;border-radius:2px}
.signer{position:absolute;left:27px;top:266px;font-size:5px;font-weight:600;line-height:6px}
.signer span{display:block;font-size:3.6px;font-weight:400;color:var(--muted)}
.fold{position:absolute;left:0;width:8px;height:.5px;background:var(--ink)}
.letter-footer{position:absolute;left:20px;right:20px;top:330px;border-top:.6px solid var(--ink);padding-top:5px;display:flex;justify-content:space-between;font-size:2.3px;line-height:2.9px}
.letter-footer div{padding-right:4px;border-right:.5px solid var(--ink)}
.letter-footer div:last-child{border-right:none}
.envelope{position:absolute;left:201px;width:296px;height:153px;background:linear-gradient(135deg,#fff,#f1f1f1);box-shadow:0 1px 4px rgba(0,0,0,.18);overflow:hidden}
.envelope-front{top:770px}
.envelope-front .brand{left:22px;top:28px;width:60px}
.address-window{position:absolute;left:21px;top:83px;width:117px;height:54px;background:var(--window);border-radius:3px}
.envelope-back{top:943px}
.envelope-flap{position:absolute;left:0;top:0;width:296px;height:47px}
.envelope-back .brand{right:14px;top:110px;width:60px}
</style>
</head>
<body>
<main class="canvas">

  <section class="card card-front" style="left:96px;top:67px">
    <div class="brand"><span class="brand-dot"></span><span class="brand-name">KLARWEG</span></div>
    <div class="card-decor" role="img" aria-label="Große Markengrafik in Blau und Grün"></div>
  </section>
  <section class="card card-back" style="left:269px;top:67px">
    <p class="card-tagline">Grafik Wahlen</p>
    <div class="brand"><span class="brand-dot"></span><span class="brand-name">KLARWEG</span></div>
    <p class="card-address">GRAFIKWAHLEN<br>Ahornweg 7<br>D-90402 Musterstadt</p>
    <p class="card-contact">Tel: 089 / 00 00 00 - 00<br>Fax: 089 / 00 00 00 - 0000<br>Mobil: 0178 / 000 00 00<br>info@grafikwahlen.de</p>
    <svg class="card-band" viewBox="0 0 159 9" preserveAspectRatio="none"><rect x="0" y="6" width="84" height="3" fill="var(--green)"/><polygon points="80,9 88,0 159,0 159,9" fill="var(--blue)"/></svg>
  </section>
  <section class="card card-front" style="left:441px;top:67px">
    <div class="brand"><span class="brand-dot"></span><span class="brand-name">KLARWEG</span></div>
    <div class="card-decor" role="img" aria-label="Große Markengrafik in Blau und Grün"></div>
  </section>

  <section class="card card-back" style="left:96px;top:171px">
    <p class="card-tagline">Grafik Wahlen</p>
    <div class="brand"><span class="brand-dot"></span><span class="brand-name">KLARWEG</span></div>
    <p class="card-address">GRAFIKWAHLEN<br>Ahornweg 7<br>D-90402 Musterstadt</p>
    <p class="card-contact">Tel: 089 / 00 00 00 - 00<br>Fax: 089 / 00 00 00 - 0000<br>Mobil: 0178 / 000 00 00<br>info@grafikwahlen.de</p>
    <svg class="card-band" viewBox="0 0 159 9" preserveAspectRatio="none"><rect x="0" y="6" width="84" height="3" fill="var(--green)"/><polygon points="80,9 88,0 159,0 159,9" fill="var(--blue)"/></svg>
  </section>
  <section class="card card-front" style="left:269px;top:171px">
    <div class="brand"><span class="brand-dot"></span><span class="brand-name">KLARWEG</span></div>
    <div class="card-decor" role="img" aria-label="Große Markengrafik in Blau und Grün"></div>
  </section>
  <section class="card card-back" style="left:441px;top:171px">
    <p class="card-tagline">Grafik Wahlen</p>
    <div class="brand"><span class="brand-dot"></span><span class="brand-name">KLARWEG</span></div>
    <p class="card-address">GRAFIKWAHLEN<br>Ahornweg 7<br>D-90402 Musterstadt</p>
    <p class="card-contact">Tel: 089 / 00 00 00 - 00<br>Fax: 089 / 00 00 00 - 0000<br>Mobil: 0178 / 000 00 00<br>info@grafikwahlen.de</p>
    <svg class="card-band" viewBox="0 0 159 9" preserveAspectRatio="none"><rect x="0" y="6" width="84" height="3" fill="var(--green)"/><polygon points="80,9 88,0 159,0 159,9" fill="var(--blue)"/></svg>
  </section>

  <section class="card card-front" style="left:96px;top:275px">
    <div class="brand"><span class="brand-dot"></span><span class="brand-name">KLARWEG</span></div>
    <div class="card-decor" role="img" aria-label="Große Markengrafik in Blau und Grün"></div>
  </section>
  <section class="card card-back" style="left:269px;top:275px">
    <p class="card-tagline">Grafik Wahlen</p>
    <div class="brand"><span class="brand-dot"></span><span class="brand-name">KLARWEG</span></div>
    <p class="card-address">GRAFIKWAHLEN<br>Ahornweg 7<br>D-90402 Musterstadt</p>
    <p class="card-contact">Tel: 089 / 00 00 00 - 00<br>Fax: 089 / 00 00 00 - 0000<br>Mobil: 0178 / 000 00 00<br>info@grafikwahlen.de</p>
    <svg class="card-band" viewBox="0 0 159 9" preserveAspectRatio="none"><rect x="0" y="6" width="84" height="3" fill="var(--green)"/><polygon points="80,9 88,0 159,0 159,9" fill="var(--blue)"/></svg>
  </section>
  <section class="card card-front" style="left:441px;top:275px">
    <div class="brand"><span class="brand-dot"></span><span class="brand-name">KLARWEG</span></div>
    <div class="card-decor" role="img" aria-label="Große Markengrafik in Blau und Grün"></div>
  </section>

  <article class="letter letter-left" style="left:99px;top:393px">
    <div class="brand"><span class="brand-dot"></span><span class="brand-name">KLARWEG</span></div>
    <p class="sender-line">GRAFIKWAHLEN | Ahornweg 7 | D-90402 Musterstadt</p>
    <div class="recipient"><p class="recipient-name">Name Surname</p>Senior Executive<br>Address goes here. Street, City, Country<br>contact@yourmail.com<br>000-987-654-321</div>
    <p class="letter-date">Date, 10 September, 2030</p>
    <div class="letter-body">
      <p>Lorem ipsum dolor sit amet, consectetur adipisicing elit, sed do eiusmod tempor incididunt ut labore et dolore magna aliqua. Ut enim ad minim veniam, quis nostrud exercitation ullamco laboris nisi ut aliquip ex ea commodo consequat. Duis aute irure dolor in reprehenderit in voluptate velit esse cillum dolore eu fugiat nulla pariatur. Excepteur sint occaecat cupidatat non proident, sunt in culpa qui officia deserunt mollit anim id est laborum. Sed ut perspiciatis unde omnis iste natus error sit voluptatem accusantium doloremque laudantium, totam rem aperiam, eaque ipsa quae ab illo inventore veritatis et quasi architecto beatae vitae dicta sunt explicabo. Nemo enim ipsam voluptatem quia voluptas sit aspernatur aut odit aut fugit, sed quia consequuntur magni dolores eos qui ratione voluptatem sequi nesciunt. Neque porro voluptatem sequi nesciunt.</p>
      <p>Lorem ipsum dolor sit amet, consectetur adipisicing elit, sed do eiusmod tempor incididunt ut labore et dolore magna aliqua. Ut enim ad minim veniam, quis nostrud exercitation ullamco laboris nisi ut aliquip ex ea commodo consequat. Duis aute irure dolor in reprehenderit in voluptate velit esse cillum dolore eu fugiat nulla pariatur. Excepteur sint occaecat cupidatat non proident, sunt in culpa qui officia deserunt mollit anim id est laborum. Sed ut perspiciatis unde omnis iste natus error sit voluptatem accusantium doloremque laudantium, totam rem aperiam, eaque ipsa quae ab illo inventore veritatis et quasi architecto beatae vitae dicta sunt explicabo.</p>
      <p>Lorem ipsum dolor sit amet, consectetur adipisicing elit, sed do eiusmod tempor incididunt ut labore et dolore magna aliqua. Ut enim ad minim veniam, quis nostrud exercitation ullamco laboris nisi ut aliquip ex ea commodo consequat.</p>
    </div>
    <div class="signature" role="img" aria-label="Handschriftliche Unterschrift"></div>
    <p class="signer">NAME SURNAME<span>General Manager</span></p>
    <span class="fold" style="top:125px"></span>
    <span class="fold" style="top:176px"></span>
    <span class="fold" style="top:250px"></span>
    <footer class="letter-footer">
      <div>Geschäftsführung:<br>Anna Berger<br>Sitz der Gesellschaft</div>
      <div>Amtsgericht Musterstadt HRB 0000<br>USt-IdNr. DE000000000<br>Steuer-Nr. 000/000/0000</div>
      <div>Musterbank Nord<br>IBAN DE00 0000 0000 0000<br>BIC MUSTDEXX</div>
      <div>Stadtsparkasse Süd<br>IBAN DE00 0000 0000 0001<br>BIC STADDEXX</div>
    </footer>
  </article>

  <article class="letter letter-right" style="left:355px;top:393px">
    <div class="brand"><span class="brand-dot"></span><span class="brand-name">KLARWEG</span></div>
    <div class="recipient"><p class="recipient-name">Name Surname</p>Senior Executive<br>Address goes here. Street, City, Country<br>contact@yourmail.com<br>000-987-654-321</div>
    <p class="letter-date">Date, 10 September, 2030</p>
    <div class="letter-body">
      <p>Lorem ipsum dolor sit amet, consectetur adipisicing elit, sed do eiusmod tempor incididunt ut labore et dolore magna aliqua. Ut enim ad minim veniam, quis nostrud exercitation ullamco laboris nisi ut aliquip ex ea commodo consequat. Duis aute irure dolor in reprehenderit in voluptate velit esse cillum dolore eu fugiat nulla pariatur. Excepteur sint occaecat cupidatat non proident, sunt in culpa qui officia deserunt mollit anim id est laborum. Sed ut perspiciatis unde omnis iste natus error sit voluptatem accusantium doloremque laudantium, totam rem aperiam, eaque ipsa quae ab illo inventore veritatis et quasi architecto beatae vitae dicta sunt explicabo. Nemo enim ipsam voluptatem quia voluptas sit aspernatur aut odit aut fugit, sed quia consequuntur magni dolores eos qui ratione voluptatem sequi nesciunt. Neque porro voluptatem sequi nesciunt.</p>
      <p>Lorem ipsum dolor sit amet, consectetur adipisicing elit, sed do eiusmod tempor incididunt ut labore et dolore magna aliqua. Ut enim ad minim veniam, quis nostrud exercitation ullamco laboris nisi ut aliquip ex ea commodo consequat. Duis aute irure dolor in reprehenderit in voluptate velit esse cillum dolore eu fugiat nulla pariatur. Excepteur sint occaecat cupidatat non proident, sunt in culpa qui officia deserunt mollit anim id est laborum. Sed ut perspiciatis unde omnis iste natus error sit voluptatem accusantium doloremque laudantium, totam rem aperiam, eaque ipsa quae ab illo inventore veritatis et quasi architecto beatae vitae dicta sunt explicabo.</p>
      <p>Lorem ipsum dolor sit amet, consectetur adipisicing elit, sed do eiusmod tempor incididunt ut labore et dolore magna aliqua. Ut enim ad minim veniam, quis nostrud exercitation ullamco laboris nisi ut aliquip ex ea commodo consequat.</p>
    </div>
    <div class="signature" role="img" aria-label="Handschriftliche Unterschrift"></div>
    <p class="signer">NAME SURNAME<span>General Manager</span></p>
    <span class="fold" style="top:112px"></span>
    <span class="fold" style="top:164px"></span>
    <span class="fold" style="top:238px"></span>
  </article>

  <section class="envelope envelope-front">
    <div class="brand"><span class="brand-dot"></span><span class="brand-name">KLARWEG</span></div>
    <div class="address-window"></div>
  </section>
  <section class="envelope envelope-back">
    <svg class="envelope-flap" viewBox="0 0 296 47" preserveAspectRatio="none"><path d="M0 0 H296 L284 32 Q279 46 264 46 H32 Q17 46 12 32 Z" fill="var(--blue)"/></svg>
    <div class="brand"><span class="brand-dot"></span><span class="brand-name">KLARWEG</span></div>
  </section>

</main>
</body>
</html>
```